Business Card Design Project

This is to go hand in hand with our stationery project.
Target Market(s)
Business Professionals in the Finance, HR and C-Level management arena. They are global companies that run enterprise technology solutions/products.
Mostly Male, mid 30's to 60's.
Industry/Entity Type
Business
Font styles to use
Other font styles liked:
- Calibri
Colors
9bcb3c
000000
1b1b1b
c4c4c4
ffffff
Requirements
Must have
- Logo
Name, title, contact details, address on the front of the card.
ABN and web address need to be on the card, along with our tag line
See | Share | Do
We also require rounded corners and for the card to be landscape please.
Our green is
C98 M0 Y93 K0
Modern, contemporary and must have white space for people to write on.
Nice to have
- Consistent elements with the stationery design.
Should not have
- No 90's waves - We want the feeling of movement but no wavey lines.

```html
<!DOCTYPE html>
<html lang="en">
<head>
<meta charset="utf-8">
<title>Nolvex Business Solutions – Business Card</title>
<link rel="stylesheet" href="https://fonts.googleapis.com/css2?family=Carlito:wght@400;700&family=Open+Sans:wght@400;600&family=Didact+Gothic&display=swap">
<style>
  :root {
    --green: #9bcb3c;
    --black: #000000;
    --ink: #1b1b1b;
    --silver: #c4c4c4;
    --white: #ffffff;
    --stage: #2f2c2a;
    --charcoal: #3a3939;
    --faint: #efeeee;
    --label: #e6e6e6;
  }
  * { box-sizing: border-box; margin: 0; padding: 0; }
  html, body { width: 1000px; height: 1200px; overflow: hidden; }
  body { background: var(--stage); position: relative; font-family: "Carlito", "Calibri", sans-serif; }

  .side-label { position: absolute; color: var(--label); font: 400 20px "Open Sans", sans-serif; }
  .side-label--front { left: 140px; top: 588px; }
  .side-label--back { left: 799px; top: 1114px; }

  .card {
    position: absolute; width: 720px; height: 436px;
    border-radius: 30px; overflow: hidden; background: var(--white);
  }
  .card--front { left: 140px; top: 120px; }
  .card--back { left: 126px; top: 638px; }

  /* front */
  .backdrop-circle {
    position: absolute; left: 433px; top: 62px; width: 244px; height: 244px;
    border-radius: 50%; background: var(--faint);
  }
  .brand-mark {
    position: absolute; left: 44px; top: 92px;
    display: flex; align-items: center; gap: 12px;
    font: 700 30px "Carlito", sans-serif; color: var(--ink); line-height: 1.1;
    white-space: nowrap;
  }
  .brand-mark .dot { width: 22px; height: 22px; border-radius: 50%; background: var(--green); flex: none; }
  .abn { position: absolute; right: 43px; top: 77px; font: 400 15.5px "Open Sans", sans-serif; color: var(--ink); }
  .holder { position: absolute; left: 44px; top: 234px; }
  .holder__name { font: 400 29px "Didact Gothic", sans-serif; color: var(--black); line-height: 1.1; letter-spacing: 0.3px; -webkit-text-stroke: 0.9px var(--black); }
  .holder__title { font: 400 23px "Didact Gothic", sans-serif; color: var(--black); line-height: 1.1; margin-top: 2px; }
  .tagline { position: absolute; right: 43px; top: 262px; font: 400 30px "Carlito", sans-serif; color: var(--ink); white-space: nowrap; }
  .tagline .sep, .tagline-back .sep { color: var(--green); }
  .rule { position: absolute; left: 18px; right: 18px; top: 315px; height: 4px; background: var(--green); }
  .contact { position: absolute; font: 400 16px "Open Sans", sans-serif; color: var(--ink); display: flex; gap: 7px; align-items: flex-start; line-height: 22px; white-space: nowrap; }
  .contact svg { width: 18px; height: 18px; margin-top: 2px; flex: none; }
  .contact--phone { right: 372px; top: 340px; }
  .contact--email { right: 372px; top: 371px; }
  .contact--fax { left: 370px; top: 340px; }
  .contact--address { left: 370px; top: 371px; }

  /* back */
  .back-top {
    position: absolute; left: 0; top: 0; width: 100%; height: 290px;
    background: radial-gradient(ellipse 380px 260px at 45% 10%, #6e6c6c 0%, #4a4949 45%, var(--charcoal) 100%);
  }
  .back-rule { position: absolute; left: 0; right: 0; top: 289px; height: 5px; background: var(--green); }
  .back-brand {
    position: absolute; left: 0; right: 0; top: 76px;
    display: flex; justify-content: center; align-items: center; gap: 16px;
    font: 700 76px "Carlito", sans-serif; color: var(--white); line-height: 1.2;
  }
  .back-brand .dot { width: 30px; height: 30px; border-radius: 50%; background: var(--green); }
  .back-sub { position: absolute; left: 0; right: 0; top: 175px; text-align: center; font: 400 31px "Carlito", sans-serif; color: var(--white); }
  .tagline-back { position: absolute; left: 0; right: 0; top: 216px; text-align: center; font: 700 24px "Carlito", sans-serif; color: var(--silver); }
  .web { position: absolute; left: 0; right: 0; top: 252px; text-align: center; font: 700 18px "Open Sans", sans-serif; color: var(--green); letter-spacing: 2px; }
</style>
</head>
<body>
  <section class="card card--front" aria-label="Business card front">
    <div class="backdrop-circle" aria-hidden="true"></div>
    <div class="brand-mark"><span class="dot"></span><span class="name">Nolvex<br>Business Solutions</span></div>
    <p class="abn">ABN 00 000 000 000</p>
    <div class="holder">
      <p class="holder__name">Daniel Reyes</p>
      <p class="holder__title">Manager</p>
    </div>
    <p class="tagline">Plan <span class="sep">•</span> Build <span class="sep">•</span> Grow</p>
    <div class="rule"></div>

    <p class="contact contact--phone">+61 (02) 5550 1286
      <svg viewBox="0 0 24 24" aria-hidden="true"><path fill="#9bcb3c" d="M6.6 2.5l3 3.6-1.8 2.3c1.2 2.6 3.2 4.6 5.8 5.8l2.3-1.8 3.6 3-2 3.6C10.4 19 5 13.6 3 6.5z"/></svg>
    </p>
    <p class="contact contact--email">sales@nolvexgroup.com
      <svg viewBox="0 0 24 24" aria-hidden="true"><path fill="#9bcb3c" d="M2 6h20v13H2z"/><path fill="none" stroke="#fff" stroke-width="1.6" d="M2 6l10 8 10-8M2 19l7-7M22 19l-7-7"/></svg>
    </p>
    <p class="contact contact--fax">
      <svg viewBox="0 0 24 24" aria-hidden="true"><path fill="#9bcb3c" d="M6 2h10v6H6zM3 10h18v11H3z"/><path fill="#fff" d="M6 13h3v2H6zm5 0h3v2h-3zm-5 4h3v2H6zm5 0h3v2h-3z"/></svg>
      +61 (02) 5550 3917
    </p>
    <p class="contact contact--address">
      <svg viewBox="0 0 24 24" aria-hidden="true"><path fill="#9bcb3c" d="M12 1a7 7 0 0 1 7 7c0 5-7 14-7 14S5 13 5 8a7 7 0 0 1 7-7z"/><circle cx="12" cy="8" r="2.6" fill="#fff"/></svg>
      <span>Level 2, 48 Harbour Lane,<br>Kelsby, NSW 2999</span>
    </p>
  </section>
  <p class="side-label side-label--front">Front</p>

  <section class="card card--back" aria-label="Business card back">
    <div class="back-top"></div>
    <div class="back-brand"><span class="dot"></span><span>Nolvex</span></div>
    <p class="back-sub">Business Solutions</p>
    <p class="tagline-back">Plan <span class="sep">•</span> Build <span class="sep">•</span> Grow</p>
    <p class="web">www.nolvexgroup.com</p>
    <div class="back-rule"></div>
  </section>
  <p class="side-label side-label--back">Back</p>
</body>
</html>
```